Vice chair

I'm running for a position as vice chair this will be posted in the lunch room cafeteria in this package i posted logos, my picture, sample of old flyers to give you a idea i also wrote literature need help in putting it together like it to look like a million bucks goal win this election I summited lots of pdf files and jpeg look though them to help with your design feel free to contact me to further assist you
Updates

Would like this to be completed by Wednesday

Target Market(s)

My constituents

Font styles to use
Serif

Colors

Designer to choose colors to be used in the design.

Requirements
Must have
• Make it look clean neat
Nice to have
• Nice background

```html
<!DOCTYPE html>
<html lang="en">
<head>
<meta charset="utf-8">
<title>Vote Independent – Vice Chair</title>
<link rel="stylesheet" href="https://fonts.googleapis.com/css2?family=Open+Sans:wght@400;600;700&family=Roboto:wght@700;900&display=swap">
<style>
  :root {
    --page-bg: #e9e9ea;
    --navy: #0f2f7a;
    --blue-deep: #0b3a8f;
    --blue-light: #2f74d4;
    --red: #d3172b;
    --red-deep: #a80d1e;
    --red-bright: #e8303f;
    --white: #ffffff;
    --ink: #2b2b2b;
    --gold: #d6a21e;
  }
  * { box-sizing: border-box; margin: 0; padding: 0; }
  html, body { width: 707px; height: 1200px; overflow: hidden; background: var(--page-bg); }
  .flyer {
    position: absolute; left: 0; top: 99px;
    width: 707px; height: 1002px; overflow: hidden;
    background: var(--white);
    font-family: "Open Sans", sans-serif;
    box-shadow: 0 3px 10px rgba(0,0,0,.18);
  }
  .backdrop { position: absolute; inset: 0; }
  .candidate-photo {
    position: absolute; left: 24px; top: 36px; width: 232px; height: 401px;
    background: linear-gradient(180deg, #caa58a 0%, #b48a6d 50%, #2a2a2a 74%, #151515 100%);
    border-radius: 110px 110px 0 0;
    border: 3px solid var(--white); border-bottom: none;
  }
  .depot-badges { position: absolute; top: 46px; left: 307px; display: flex; gap: 20px; }
  .depot-badge {
    width: 105px; height: 105px; border-radius: 50%;
    border: 4px solid var(--white);
  }
  .depot-badge.west { background: #3d6fb8; }
  .depot-badge.kings { background: #e8792a; }
  .depot-badge.gun { background: #f2d21c; }
  .headline {
    position: absolute; left: 350px; top: 284px; width: 324px;
    font-family: "Roboto", sans-serif; font-weight: 900;
    font-size: 128px; line-height: 1; letter-spacing: -2px;
    color: var(--red);
    background: linear-gradient(180deg, #ef4655 0%, #c0101f 100%);
    -webkit-background-clip: text; background-clip: text; -webkit-text-fill-color: transparent;
    text-align: center;
  }
  .subhead {
    position: absolute; left: 352px; top: 400px; width: 320px;
    font-family: "Roboto", sans-serif; font-weight: 700; font-size: 29px;
    color: var(--navy); text-align: right; letter-spacing: .5px;
  }
  .intro {
    position: absolute; top: 456px;
    font-size: 13.2px; line-height: 19.4px; color: var(--ink); text-align: justify;
  }
  .intro.left { left: 31px; width: 290px; }
  .intro.right { left: 351px; width: 322px; }
  .platform {
    position: absolute; left: 40px; top: 732px; width: 400px;
    list-style: none; color: var(--white); font-size: 11.3px; line-height: 16px;
  }
  .platform li { position: relative; padding-left: 18px; margin-bottom: 9px; }
  .platform li::before {
    content: ""; position: absolute; left: 2px; top: 5px;
    width: 6px; height: 6px; border-radius: 50%; background: var(--white);
  }
  .platform .closing::before { display: none; }
  .slate-arc { position: absolute; left: 436px; top: 700px; width: 250px; height: 100px; }
  .slate-mark {
    position: absolute; left: 537px; top: 750px; width: 42px; height: 40px;
    background: var(--white); border: 2px solid var(--navy);
    color: var(--navy); font-family: "Roboto", sans-serif; font-weight: 900;
    font-size: 34px; line-height: 36px; text-align: center;
  }
  .union-name {
    position: absolute; left: 450px; top: 866px; width: 236px;
    display: flex; align-items: center; gap: 10px;
  }
  .union-name .dot { width: 46px; height: 46px; border-radius: 50%; background: var(--gold); flex: none; }
  .union-name span {
    font-family: "Open Sans", sans-serif; font-weight: 700; font-size: 20px;
    line-height: 24px; color: var(--white);
  }
</style>
</head>
<body>
<main class="flyer">
  <svg class="backdrop" viewBox="0 0 707 1002" width="707" height="1002" aria-hidden="true">
    <defs>
      <linearGradient id="sky" x1="0" y1="0" x2="0" y2="1">
        <stop offset="0" stop-color="#0b3a8f"/>
        <stop offset="1" stop-color="#2f74d4"/>
      </linearGradient>
      <linearGradient id="field" x1="0" y1="0" x2="0" y2="1">
        <stop offset="0" stop-color="#e8303f"/>
        <stop offset="1" stop-color="#a80d1e"/>
      </linearGradient>
    </defs>
    <path d="M0 0 H707 V250 C600 246 470 242 380 228 C330 220 300 190 261 186 L0 186 Z" fill="url(#sky)"/>
    <path d="M0 176 H261 C300 180 330 208 380 216 C470 230 600 234 707 236 V252 C600 250 470 248 378 236 C330 228 300 200 261 196 H0 Z" fill="#ffffff"/>
    <path d="M0 186 H261 C300 190 330 216 380 224 C470 238 600 241 707 243 V250 C600 248 470 245 378 232 C330 224 300 196 261 192 H0 Z" fill="#d3172b"/>
    <path d="M0 168 H255 C298 172 330 198 380 206 C470 220 600 224 707 226 V238 C600 236 470 232 380 218 C330 210 300 182 261 180 H0 Z" fill="#2f74d4"/>
    <g fill="#ffffff">
      <circle cx="12" cy="174" r="3"/><circle cx="300" cy="186" r="3"/><circle cx="330" cy="200" r="3"/>
      <circle cx="400" cy="214" r="3"/><circle cx="460" cy="221" r="3"/><circle cx="520" cy="226" r="3"/>
      <circle cx="580" cy="229" r="3"/><circle cx="640" cy="231" r="3"/><circle cx="690" cy="232" r="3"/>
    </g>
    <path d="M0 700 C110 640 220 618 320 628 C450 640 560 690 707 686 V1002 H0 Z" fill="#0f2f7a"/>
    <path d="M0 720 C110 660 220 640 320 650 C450 662 560 710 707 706 V1002 H0 Z" fill="#ffffff"/>
    <path d="M0 730 C110 672 220 652 320 662 C450 674 560 720 707 716 V1002 H0 Z" fill="url(#field)"/>
  </svg>

  <div class="candidate-photo" role="img" aria-label="Portrait photo of the candidate, Daniel Ortiz"></div>

  <div class="depot-badges">
    <div class="depot-badge west" role="img" aria-label="Depot badge"></div>
    <div class="depot-badge kings" role="img" aria-label="Depot badge"></div>
    <div class="depot-badge gun" role="img" aria-label="Depot badge"></div>
  </div>

  <h1 class="headline">VOTE</h1>
  <p class="subhead">INDEPENDENT [X]</p>

  <p class="intro left">I Daniel Ortiz for those who don't know me would like to introduce myself I have always been approachable and helpful whether you are a probationary officer or a veteran operator with knowledge or information. We must protect our union rules for ourselves our future and most important our children.</p>
  <p class="intro right">I would like this opportunity to run as your vice chair a person you can trust and believe in me Positive and motivations are my main keys for progress and for change in my campaign When there are no leaders to lookup to one therefore must become one I do believe I'm the right person for this position so please come out and support me and vote me as your vice chair</p>

  <ul class="platform">
    <li>20 years on the job</li>
    <li>Past union member of Freight Workers Local 412 believes in There is a collective bargaining agreement in place and no management is above the law to violate it</li>
    <li>Past union member of Cargo Workers Local 630 believes a house that is divided cannot stand alone</li>
    <li>In closing I believe that our union does not stand out individually achievement we must stand for collective advancement for all. we must always continue to stand together, stay together &amp; fight together so we can win together because success is never owned, it is rented and the rent is due every day.</li>
    <li class="closing">Vote independent me as your vice chair</li>
  </ul>

  <svg class="slate-arc" viewBox="0 0 250 100" aria-label="Vote the slate">
    <path id="slateCurve" d="M10 62 Q125 10 240 74" fill="none"/>
    <text font-family="Roboto, sans-serif" font-weight="900" font-size="29" fill="#ffffff">
      <textPath href="#slateCurve" startOffset="50%" text-anchor="middle">Vote the slate</textPath>
    </text>
  </svg>
  <div class="slate-mark">X</div>

  <div class="union-name">
    <div class="dot"></div>
    <span>Riders Union Alliance</span>
  </div>
</main>
</body>
</html>
```